Awesome business card design needed

We need a new business card design to go with our new logo.
We are a web development agency that specialises in highly complex back-end integrations as opposed to design, our customers are retailers, hotels, hospitals and any other organisation that has a large online marketing department.
Take a look at our website - www.kotravelu.com for some inspiration.
We want our new business cards to exude class, professionalism and style.
We are likely to choose a high-end card to print them on but we want the design of the card itself to really turn heads.
We have no specific colour requirements, the logo as you will see is a turquoise colour R89 G171 B167 #59aba7 but it can also be in white if you want to make the colour of the card something different.
The information on the card should be:
Name
Position
Tel
email
Potentially a double sided card could have our web address, twitter and FB links.

```html
<!DOCTYPE html>
<html lang="en">
<head>
<meta charset="utf-8">
<title>Kotravelu business card</title>
<link rel="stylesheet" href="https://fonts.googleapis.com/css2?family=Cinzel:wght@400;700&display=swap">
<style>
  :root {
    --page: #e4e3df;
    --card: #2f2f30;
    --card-edge: #242425;
    --teal: #59aba7;
    --white: #f2f2f0;
    --ink: #1e1e1e;
  }
  * { box-sizing: border-box; margin: 0; padding: 0; }
  html, body { width: 1200px; height: 900px; overflow: hidden; }
  body {
    background: var(--page);
    font-family: "Cinzel", serif;
    position: relative;
  }
  .card {
    position: absolute;
    left: 280px;
    width: 640px;
    height: 366px;
    background: var(--card);
    box-shadow: 0 6px 18px rgba(0,0,0,0.25);
    overflow: hidden;
  }
  .card--back { top: 50px; }
  .card--front { top: 478px; }

  .wordmark {
    color: var(--teal);
    font-weight: 700;
    letter-spacing: 2px;
    text-transform: lowercase;
    line-height: 1;
  }
  .card--back .wordmark {
    position: absolute;
    top: 120px;
    left: 0; right: 0;
    text-align: center;
    font-size: 62px;
  }
  .links {
    position: absolute;
    left: 24px; right: 24px;
    bottom: 26px;
    display: flex;
    justify-content: space-between;
    list-style: none;
    color: var(--white);
    font-size: 11px;
    letter-spacing: 0.5px;
  }
  .links__item { display: flex; align-items: center; gap: 7px; }
  .links__mark {
    width: 13px; height: 13px;
    background: var(--teal);
    flex: none;
  }

  .card--front .wordmark {
    position: absolute;
    top: 52px; left: 40px;
    font-size: 64px;
  }
  .person {
    position: absolute;
    top: 138px; right: 40px;
    text-align: right;
  }
  .person__name {
    color: var(--teal);
    font-size: 22px;
    letter-spacing: 1px;
    border-bottom: 1px solid var(--teal);
    padding-bottom: 2px;
  }
  .person__role {
    color: var(--white);
    font-size: 14px;
    margin-top: 2px;
  }
  .side-tab {
    position: absolute;
    right: 0; top: 128px;
    width: 10px; height: 44px;
    background: var(--teal);
  }
  .rule {
    position: absolute;
    left: 40px; right: 40px;
    top: 196px;
    height: 1px;
    background: var(--teal);
  }
  .contact {
    position: absolute;
    left: 40px; top: 222px;
    list-style: none;
    color: var(--white);
    font-size: 15px;
    letter-spacing: 0.5px;
  }
  .contact__item { display: flex; align-items: center; gap: 12px; height: 26px; }
  .contact__icon { width: 16px; height: 16px; flex: none; }
  .band {
    position: absolute;
    left: 0; bottom: 0;
    width: 640px; height: 110px;
  }
  .quote {
    position: absolute;
    left: 22px; bottom: 8px;
    height: 28px;
    line-height: 28px;
    color: var(--ink);
    font-size: 14px;
    font-weight: 700;
    letter-spacing: 0.5px;
    white-space: nowrap;
  }
</style>
</head>
<body>

<section class="card card--back" aria-label="Card back">
  <p class="wordmark">kotravelu</p>
  <ul class="links">
    <li class="links__item"><span class="links__mark"></span>www.kotravelu.com</li>
    <li class="links__item"><span class="links__mark"></span>social.kotravelu.com/team</li>
    <li class="links__item"><span class="links__mark"></span>news.kotravelu.com/feed</li>
  </ul>
</section>

<section class="card card--front" aria-label="Card front">
  <p class="wordmark">kotravelu</p>
  <div class="side-tab"></div>
  <div class="person">
    <p class="person__name">Marcus Ellery</p>
    <p class="person__role">President</p>
  </div>
  <div class="rule"></div>
  <ul class="contact">
    <li class="contact__item">
      <svg class="contact__icon" viewBox="0 0 16 16" aria-hidden="true">
        <path d="M3 2 L6 2 L7 5 L5.5 6.5 Q7 9.5 9.5 10.5 L11 9 L14 10 L14 13 Q13 14.5 11 14 Q4 12 2 5 Q1.8 3 3 2 Z" fill="#59aba7"/>
      </svg>
      (000) 555 - 014 - 270
    </li>
    <li class="contact__item">
      <svg class="contact__icon" viewBox="0 0 16 16" aria-hidden="true">
        <rect x="1" y="3.5" width="14" height="9" fill="none" stroke="#59aba7" stroke-width="1.4"/>
        <path d="M1 3.5 L8 9 L15 3.5 M1 12.5 L6 8 M15 12.5 L10 8" fill="none" stroke="#59aba7" stroke-width="1.2"/>
      </svg>
      info@kotravelu.com
    </li>
  </ul>
  <svg class="band" viewBox="0 0 640 110" aria-hidden="true">
    <path d="M0 74 L468 74 Q486 74 492 60 Q498 42 520 42 L640 42 L640 48 L522 48 Q504 48 498 64 Q492 84 470 102 L0 102 Z" fill="#59aba7"/>
  </svg>
  <p class="quote">"Plans are nothing; planning is everything."</p>
</section>

</body>
</html>
```